One Page / Executive Summary for Silverpine Executive Search

We would need an executive summary for our firm Silverpine Executive Search - like a small one pager which we can via PDF to our clients.
It should include like the file 23030 all Infos - Only Track Record needs to be complemented
But it should be designed much nicer than it is now - also open for new design situations but it should fit our website concept www.silverpinexs.io
It should also include a graph of the recruiting process - maybe draw a new one.?
We would need a very elegant, modern, slim design, it should look very female - it should not have a green color block on the top but be more sleek bright and with our bird
Target Market(s)
CEO, HR executives
Industry/Entity Type
HR Consultantcy
Other font styles liked:
- Calibri, cost or robotic condensed
Requirements
Must have
- sleek slim modern elegant design, ideally a white side with a frame or with our bird
Nice to have
- project progress on our website, female modern, elegant design, not too overloaded, possibility to complement our text
Should not have
- no petrol color block as on our website or as in our proposal, prefer a white background with our photo as a log,

```html
<!DOCTYPE html>
<html lang="en">
<head>
<meta charset="utf-8">
<title>Silverpine Executive Search – Executive Summary</title>
<link href="https://fonts.googleapis.com/css2?family=Josefin+Sans:wght@300&family=Playfair+Display:wght@400&family=Poppins:wght@400;500;600&family=Roboto+Condensed:wght@400&display=swap" rel="stylesheet">
<style>
:root{
  --teal:#0d5266;
  --blue:#1089c9;
  --blue-light:#23a9de;
  --red:#e8473a;
  --sky:#cfe6f1;
  --ink:#2b2b2b;
  --stage:#e8e9eb;
  --paper:#ffffff;
  --purple:#b2248f;
}
*{margin:0;padding:0;box-sizing:border-box}
html,body{width:1200px;height:2736px;overflow:hidden;background:var(--stage)}
.sheet{position:absolute;left:50px;top:657px;width:1100px;height:1421px;background:var(--paper);overflow:hidden;box-shadow:0 6px 30px rgba(0,0,0,.12)}
.abs{position:absolute}
.deco-top{left:357px;top:0;width:743px;height:306px;background:linear-gradient(120deg,var(--purple) 0%,#7a3db8 30%,var(--blue-light) 55%,#1c8fc0 75%,var(--purple) 100%);clip-path:polygon(0 0,100% 0,100% 100%,80% 71%,56% 62%,32% 33%)}
.deco-bottom{left:0;top:1242px;width:376px;height:179px;background:linear-gradient(60deg,var(--purple) 0%,var(--blue-light) 45%,#1c8fc0 70%,var(--purple) 100%);clip-path:polygon(0 0,20% 40%,45% 35%,70% 60%,100% 100%,0 100%)}
.brand-mark{left:128px;top:140px;width:230px;height:230px;border-radius:50%;background:var(--sky)}
.tagline{left:430px;top:212px;font:400 26px/1 "Poppins",sans-serif;color:var(--red)}
.brand-name{left:356px;top:268px;width:620px;font:300 104px/1 "Josefin Sans",sans-serif;color:var(--teal);letter-spacing:6px;white-space:nowrap}
.values{left:121px;top:422px;width:857px;display:flex;gap:6px}
.values span{flex:1;height:45px;background:var(--blue);border-left:5px solid var(--blue-light);border-right:5px solid var(--blue-light);border-radius:0 0 10px 10px;color:#fff;font:400 27px/45px "Poppins",sans-serif;text-align:center}
.section-title{left:0;width:1100px;top:474px;text-align:center;font:400 86px/1 "Playfair Display",serif;color:var(--teal)}
.col-left{left:116px;top:567px;width:410px}
.col-right{left:570px;top:567px;width:420px}
.icon{width:67px;height:67px;display:block}
.service-title{margin-top:18px;font:600 30px/1.1 "Poppins",sans-serif;color:#111}
.body{margin-top:10px;font:400 16.5px/1.0 "Roboto Condensed",sans-serif;color:var(--ink);text-align:justify}
.heading{font:400 46px/1.1 "Playfair Display",serif;color:var(--teal)}
.process-title{left:116px;top:1072px;white-space:nowrap}
.checks{display:grid;grid-template-columns:215px 190px;column-gap:10px;margin-top:4px}
.checks ul{list-style:none}
.checks li{position:relative;padding-left:16px;font:400 16px/1.0 "Roboto Condensed",sans-serif;color:var(--ink);margin-bottom:14px}
.checks li::before{content:"";position:absolute;left:0;top:3px;width:5px;height:9px;border:solid var(--red);border-width:0 2.5px 2.5px 0;transform:rotate(40deg)}
.dot-list{list-style:none;font:500 18.5px/1.05 "Poppins",sans-serif;color:var(--red)}
.dot-list li{position:relative;padding-left:32px}
.dot-list li::before{content:"";position:absolute;left:2px;top:5px;width:14px;height:14px;border-radius:50%;background:var(--sky)}
.industries{display:grid;grid-template-columns:202px 200px;row-gap:10px;margin-top:8px}
.directors{display:flex;align-items:center;margin-top:10px}
.portrait{width:118px;height:118px;border-radius:50%;border:4px solid #1a1a1a;background:radial-gradient(circle at 50% 40%,#f0a89c,var(--red) 60%,#222 100%);flex:none}
.names{margin-left:10px;width:278px;border-top:2px solid var(--teal);border-bottom:2px solid var(--teal);padding:28px 0 26px 7px;font:500 18px/1.3 "Poppins",sans-serif;color:var(--teal)}
.numbers li{margin-bottom:8px}
.process{left:125px;top:1128px;width:400px;height:160px}
.cta{left:386px;top:1330px;width:170px;height:20px;background:var(--blue);color:#fff;font:500 14px/20px "Poppins",sans-serif;padding-left:16px;clip-path:polygon(0 0,100% 0,96% 100%,0 100%)}
.footer{left:376px;top:1349px;width:724px;height:72px;background:var(--red);clip-path:polygon(0 0,100% 0,100% 100%,8% 100%)}
.contact{font:400 18px/1 "Poppins",sans-serif;color:#fff;position:absolute}
.social{left:968px;top:1362px;display:flex;flex-direction:column;gap:6px}
.social i{display:block;width:13px;height:13px;border-radius:50%;background:#fff}
</style>
</head>
<body>
<main class="sheet">
  <div class="abs deco-top" role="img" aria-label="Faceted low-poly crystal decoration in magenta, violet and turquoise"></div>
  <div class="abs deco-bottom" role="img" aria-label="Faceted low-poly crystal decoration in magenta, violet and turquoise"></div>

  <div class="abs brand-mark"></div>
  <p class="abs tagline">So, they don’t wear ties in the<br>boardrooms anymore. We never did...</p>
  <h1 class="abs brand-name">SILVERPINE</h1>

  <div class="abs values"><span>Honest</span><span>Personal</span><span>Pragmatic</span><span>Diverse</span></div>

  <h2 class="abs section-title">Services</h2>

  <section class="abs col-left">
    <svg class="icon" viewBox="0 0 67 67" fill="none" stroke="#1089c9" stroke-width="3">
      <path d="M2 14V2h12M53 2h12v12M65 53v12H53M14 65H2V53"/>
      <circle cx="33.5" cy="33.5" r="22"/><circle cx="33.5" cy="33.5" r="14"/>
      <circle cx="33.5" cy="29" r="5"/><path d="M24 43c2-6 17-6 19 0"/>
      <path d="M33.5 6v8M33.5 53v8M6 33.5h8M53 33.5h8"/>
    </svg>
    <h3 class="service-title">Executive Search</h3>
    <p class="body">We are helping you to identify and hire highly qualified and experienced candidates for senior-level executive positions. Our goal is to identify the most qualified candidates and match them with the needs and culture of your company.</p>

    <h3 class="heading" style="margin-top:10px">Why us?</h3>
    <div class="checks">
      <ul>
        <li>Longstanding experience with a passion for placing C-Level Executives</li>
        <li>We work with you personally and act as an ambassador for our clients in the market</li>
        <li>Engaging in at eye-level discussion beyond just placement and HR topics</li>
        <li>Structured, lean and, most importantly, transparent digital processes,</li>
      </ul>
      <ul>
        <li>with the opportunity of 24/7 self-update on search status in our online tool</li>
        <li>Creative search approaches and comprehensive candidate evaluation</li>
        <li>Through referencing of candidates as part of the process; psychometrics on demand</li>
      </ul>
    </div>
  </section>

  <h3 class="abs heading process-title">Recruiting Process</h3>

  <svg class="abs process" viewBox="0 0 400 160" font-family="Roboto Condensed, sans-serif" text-anchor="middle">
    <g fill="#0d5266" font-size="7">
      <text x="75" y="8">Phase 1</text><text x="75" y="17">Research - LONGLIST</text>
      <text x="200" y="8">Phase 2</text><text x="200" y="17">Fokus &amp; Interviews - SHORTLIST</text>
      <text x="315" y="8">Phase 3</text><text x="315" y="17">Abschluss</text>
      <text x="26" y="26">KW 1</text><text x="385" y="26">KW 12</text>
    </g>
    <line x1="20" y1="30" x2="392" y2="30" stroke="#e8473a" stroke-width="1.5"/>
    <g stroke="#0d5266" stroke-width="1">
      <line x1="38" y1="30" x2="38" y2="52"/><line x1="100" y1="30" x2="100" y2="104"/>
      <line x1="168" y1="30" x2="168" y2="52"/><line x1="258" y1="30" x2="258" y2="104"/>
      <line x1="330" y1="30" x2="330" y2="52"/>
    </g>
    <circle cx="38" cy="60" r="9" fill="#cfe6f1"/>
    <circle cx="100" cy="112" r="9" fill="#8ac4dc"/>
    <circle cx="168" cy="60" r="9" fill="#5da9cc"/>
    <circle cx="258" cy="112" r="9" fill="#1089c9"/>
    <circle cx="330" cy="60" r="9" fill="#0d5266"/>
    <g font-size="7" fill="#555">
      <text x="38" y="80">Kickoff</text><text x="38" y="89">Briefing and profile</text>
      <text x="100" y="132">Research</text><text x="100" y="141">Market mapping</text>
      <text x="168" y="80">Interviews</text><text x="168" y="89">Candidate talks</text>
      <text x="258" y="132">Referenzen</text><text x="258" y="141">Reference checks</text>
      <text x="330" y="80">Kandidatenauswahl</text><text x="330" y="89">Offer and onboarding</text>
    </g>
  </svg>

  <section class="abs col-right">
    <svg class="icon" viewBox="0 0 67 67" fill="none" stroke="#1089c9" stroke-width="3" stroke-linejoin="round">
      <rect x="24" y="3" width="38" height="30" rx="3"/>
      <path d="M32 24l8-8 6 5 9-10"/>
      <circle cx="20" cy="36" r="7"/><path d="M6 64c0-12 6-18 14-18s14 6 14 18z"/>
    </svg>
    <h3 class="service-title">Leadership Advisory</h3>
    <p class="body">Our Leadership advisory services are for Management Teams as well as HR-Professionals and candidates. They are designed to help you, and your organization, to build strong and effective leadership skills and teams that can drive growth, innovation, and success.</p>

    <h3 class="heading" style="margin-top:16px">Industries</h3>
    <ul class="dot-list industries">
      <li>Healthcare</li><li>Consumer</li>
      <li>Private Capital</li><li>Education<br>&amp; Administration</li>
    </ul>

    <h3 class="heading" style="margin-top:6px">Managing Directors</h3>
    <div class="directors">
      <div class="portrait" role="img" aria-label="Portrait photo of the two managing directors"></div>
      <p class="names">Dr. Clara Weissenbach<br>Lena Hofstetter</p>
    </div>

    <h3 class="heading" style="margin-top:6px">By the numbers</h3>
    <ul class="dot-list numbers" style="margin-top:8px">
      <li>xx% placement rate</li>
      <li>Xx days to placement</li>
      <li>95% retention rate over the course<br>of two years</li>
      <li>20+ years total of experience in the<br>Executive search sector</li>
    </ul>
  </section>

  <div class="abs cta">Lets work together:</div>
  <div class="abs footer"></div>
  <p class="contact" style="left:462px;top:1360px">✉ office@silverpinexs.io</p>
  <p class="contact" style="left:462px;top:1386px">✆ 09876/5432</p>
  <p class="contact" style="left:708px;top:1373px">◍ www.silverpinexs.io</p>
  <div class="abs social"><i></i><i></i><i></i></div>
</main>
</body>
</html>
```